Job Coaching - Falo; engaging people to improve their work experience

design a website focussed on people
with 4 tabs/pages (+2)
1) landing page
2) Professional
3) Job Coaching
4) Bio
5) Contact
6) references

I've added the text to be used in the documents. The website will be in Dutch, but I've added the translations in green just for you to understand what it is about.

I've added my logo as well, and a flyer I used already. this gives you an idea on how it could look like
Pictures you can find there as well. Other pictures can be added of course
The techical creation of the website is not needed. I need all the designs and information to be able to create it myself.

```html
<!DOCTYPE html>
<html lang="en">
<head>
<meta charset="utf-8">
<title>Falo – Job Coaching</title>
<link href="https://fonts.googleapis.com/css2?family=Poppins:wght@400;500;600;700;800&display=swap" rel="stylesheet">
<style>
:root{
  --ink:#1a1a1a;
  --white:#ffffff;
  --hero-deep:#1b6f8c;
  --hero-mid:#1f9cc0;
  --hero-light:#2bb1d4;
  --teal:#3aa99c;
  --green:#1cc08c;
  --grey-band:#ebebeb;
  --footer:#000000;
  --badge-blue:#1f4f8f;
  --badge-green:#4c8f2e;
  --illus-blue:#dfe9fb;
}
*{box-sizing:border-box;margin:0;padding:0}
html,body{width:1200px;height:3125px;overflow:hidden;background:var(--white)}
body{position:relative;font-family:"Poppins",sans-serif;color:var(--ink)}
.abs{position:absolute}

/* Navigation */
.site-nav{top:0;left:0;width:1200px;height:46px;background:var(--white)}
.brand{left:97px;top:6px;height:36px;display:flex;align-items:center;gap:8px;border-left:1px solid #ccc;padding-left:10px}
.brand-mark{width:22px;height:22px;border-radius:50%;background:var(--teal)}
.brand-name{font-size:24px;font-weight:600;color:var(--teal);letter-spacing:1px}
.nav-links a{position:absolute;top:18px;font-size:12px;color:var(--ink);text-decoration:none}

/* Hero */
.hero{top:46px;left:0;width:1200px;height:607px;overflow:hidden}
.hero-photo{top:0;left:0;width:1200px;height:607px;
  background:radial-gradient(ellipse at 45% 40%,var(--hero-light) 0%,var(--hero-mid) 45%,var(--hero-deep) 100%)}
.hero-title{top:74px;left:0;width:1200px;text-align:center;font-size:178px;font-weight:700;color:var(--white);letter-spacing:2px;line-height:1}
.hero-intro{top:262px;left:270px;width:660px;text-align:center;color:var(--white);font-size:11.6px;font-weight:500;line-height:16.9px}
.hero-intro strong{color:#111;font-weight:600}

/* Sections */
.section-title{font-size:51px;font-weight:400;line-height:1}
.body-copy{font-size:11px;line-height:16.3px}
.illustration{border-radius:20px}

.teal-arc{right:0;top:850px;width:125px;height:836px}

.cta{left:344px;top:1820px;width:305px;height:54px;border-radius:14px;background:var(--green);color:var(--white);font-size:19px;font-weight:700;display:flex;align-items:center;justify-content:center}

.bio-band{top:1950px;left:0;width:1200px;height:549px;background:var(--grey-band)}

.quotes-list li{list-style:none;font-size:24px;line-height:34.5px}

.site-footer{top:2885px;left:0;width:1200px;height:148px;background:var(--footer);color:var(--white)}
.footer-title{top:18px;width:1200px;text-align:center;font-size:12.5px;font-weight:600}
.footer-col{top:70px;font-size:11.5px;line-height:16.5px}

.partner-badge{top:3041px}
</style>
</head>
<body>

<header class="site-nav abs">
  <div class="brand abs"><span class="brand-mark"></span><span class="brand-name">Falo</span></div>
  <nav class="nav-links">
    <a style="left:866px">Professional</a>
    <a style="left:968px">Job Coaching</a>
    <a style="left:1077px">Bio</a>
  </nav>
</header>

<section class="hero abs">
  <div class="hero-photo abs" role="img" aria-label="Photo of a wooden figure climbing wooden steps placed by a hand, on a blue background"></div>
  <h1 class="hero-title abs">HELLO</h1>
  <p class="hero-intro abs">
    <strong>, my name is Jan Verlinden.</strong> As a passionate career coach, I want to empower you to do your job every day.<br>
    We are staying at work longer and longer, so today more than ever it is important to pay the necessary attention to professional growth and well-being at work.<br>
    I am convinced that people are often capable of more than they believe themselves to be. Everything starts with the desire for change. Who am I? What is my role? What do I really want?<br>
    As a job coach, I don't go for simple quick-wins or ready-made tips and tricks. In a spirit of openness, trust and equality, we search together for the deeper insights and sustainable solutions that work for you. Coaching is an awareness process that leads to finding the answers within yourself.<br>
    Sign up today for a no-obligation introductory consultation and take control of your career (again).
  </p>
</section>

<svg class="teal-arc abs" viewBox="0 0 125 836" aria-hidden="true"><path d="M125 0 C40 140 0 300 0 430 C0 580 60 730 125 836 Z" fill="var(--teal)"/></svg>

<!-- Professional -->
<div class="illustration abs" role="img" aria-label="Illustration of a woman holding a green heart" style="left:97px;top:710px;width:224px;height:176px;background:radial-gradient(circle at 50% 45%,#cfe0fb,var(--illus-blue) 70%,#fff)"></div>
<h2 class="section-title abs" style="left:342px;top:716px">Professional</h2>
<div class="body-copy abs" style="left:344px;top:788px;width:635px">
My job as an occupational psychologist and my many years of experience in the HR sector have taught me how important it is for employees and managers to stand in their shoes in the job they do.<br>
Often people are confronted at work with situations for which there are no simple and ready-made solutions such as (lingering) conflicts, stress, communication problems, lack of self-confidence or assertiveness, missing out on promotion opportunities, difficult career choices, skewed power relations, intimidation, coping with bad news, etc.<br>
Professional coaching is then often the most appropriate method to deal with such complex challenges in a targeted and efficient way, starting from the intrinsic strength of the coachee.<br>
In this way I have successfully coached many managers, team leaders and other experts in their growth process towards personal and professional development.<br>
Coaching not only helps you to think more consciously about the role and impact you have as a manager, colleague or employee, but also about what you yourself want and find important on a professional level and how you can achieve this.<br>
Competencies are the key to success and satisfaction. A new position or situation often requires new skills and abilities. Developing these competencies gives you the necessary self-confidence for the next step in your career. Managers and team leaders play a crucial role within their organizations. Leadership development is therefore of prime importance for the successful expansion of a company. A leader who - in a self-aware and authentic manner - can emerge as the best version of himself or herself is the best guarantee for sustainable growth and stability.<br>
Themes often addressed during leadership development include:<br>
Situational leadership<br>Authenticity<br>Coaching leadership<br>Team development<br>Change management<br>--<br>
Because every situation and every person is unique, it is important to first clearly identify the situation, the problem and the expectations.<br>
A first step is an intake conversation between the coachee, the person responsible and myself. This conversation aims to align expectations and goals so that everyone knows which themes will be worked on during the coaching conversations.<br>
Because coaching is customized, the rest of the process will then be further fine-tuned.<br>
Request your introductory meeting here/For more info on professional coaching click here
</div>

<!-- Job coaching -->
<h2 class="section-title abs" style="left:342px;top:1411px">Job coaching</h2>
<div class="body-copy abs" style="left:344px;top:1482px;width:635px">
We easily spend 8 hours a day on our professional activities, our job. If we assume that we sleep about 8 hours a day, that is therefore 50% of our active time: we see our colleagues as often or even more than our partner and/or children.<br>
Therefore, if we feel unhappy at work, this also has a huge impact on our private life. Moreover, we work longer and longer; a career today lasts more than forty years on average. It is therefore more important than ever that we spend our working time meaningfully and pay the necessary attention to personal development: after all, a young twenty-something has different professional ambitions and priorities than a fifty-something.<br>
Do you recognize yourself in any of the following questions?<br>
How can I get more energy from my job?<br>How can I find a better work-life balance?<br>What are my talents?<br>How can I work better with my manager and/or colleagues?<br>Maybe you think you have more to offer than you can show today?<br>Or do you know what you want to achieve, but don't dare to take the step?<br>--<br>
Then choose change now. Choose career counseling. Because you are worth it!<br>
Together we take a close look at your personal situation and work on a tailor-made solution.<br>
If you are entitled to AWLB career cheques, these can be used.<br>
40€ for 4 hours<br>80€ for 7 hours
</div>
<div class="cta abs">link to AWLB career cheques</div>
<div class="illustration abs" role="img" aria-label="Illustration of a man reading on a sofa" style="left:928px;top:1674px;width:267px;height:224px;background:linear-gradient(180deg,#f3f3f3,var(--illus-blue))"></div>

<!-- Biography -->
<section class="bio-band abs">
  <div class="abs" role="img" aria-label="Portrait photo of the coach in a red shirt" style="left:240px;top:51px;width:209px;height:219px;background:linear-gradient(180deg,#e4e4e4,#9c2a35 70%,#7a1f2a)"></div>
  <h2 class="section-title abs" style="left:479px;top:44px">Biography</h2>
  <div class="body-copy abs" style="left:479px;top:118px;width:520px">
  What is your profession? - is often the first question people ask each other. The job you do - and how you feel about it - largely determines a person's self-image and identity. It is therefore important to find a job that suits you.<br>
  I speak from my own experience. During my Psychology studies (KU Northfield), I consciously chose to major in Occupational Psychology. I found - and still find - the interaction between professional and personal growth and how to stimulate it downright fascinating.<br>
  The course was the starting point for my own quest. Also literally. After obtaining my Masters in Occupational Psychology, I set out on foot for Santiago de Compostela. A few years later, I walked to Rome with my (then future) wife. We walked an average of eight hours a day. How that went? Like everything else in life, step by step.
  </div>
  <div class="body-copy abs" style="left:234px;top:282px;width:762px">
  Professionally, I have also come a long way within Human Resources over the past fifteen years. I have worked in various sectors (ICT, High Tech, Telecom and metal processing), both in Belgium and abroad (China and India). As a result, I have extensive experience as a Recruiter, Business Partner, Project Manager and Talent Manager. I had the opportunity to guide professionals in their growth process and this gave me enormous satisfaction and energy.<br>
  At a certain point I followed a coaching program myself, and then I experienced what a difference it can make: thanks to coaching you become more aware of yourself and your possibilities. If you start from your own strength, you get further. Inspiration can be found along the way.<br>
  To further specialize as a coach, I took the training to become an Associated Certified Coach (ACB label) at CoachBridge. I then enrolled in the Career Coach course at the Coachstudio Noord to further expand my expertise.<br>
  Even more than my professional training and experiences, fatherhood has made me the person and coach I am today. As a father of two beautiful sons and an amazing daughter, I know it is not always easy to maintain a healthy work-life balance. Fatherhood has taught me to be mild - to others and to myself -, to communicate openly and to develop a strong bond of trust. Qualities that are indispensable as a coach.<br>
  I have found the job of my life. Will you soon too?
  </div>
</section>

<!-- Quotes -->
<h2 class="abs" style="left:366px;top:2557px;font-size:49px;font-weight:400;line-height:1">Quotes</h2>
<ul class="quotes-list abs" style="left:366px;top:2620px">
  <li>"Coaching is customization"</li>
  <li>"Coaching is awareness-raising"</li>
  <li>"Customized coaching: your key to success"</li>
  <li>"Become the best version of yourself"</li>
  <li>"Discover the power of authentic leadership"</li>
</ul>

<!-- Footer -->
<footer class="site-footer abs">
  <div class="footer-title abs">contact</div>
  <div class="footer-col abs" style="left:234px">0100-4410272<br>4120-5507721-118<br>20455-118204-7761</div>
  <div class="footer-col abs" style="left:515px">0100-4410272<br>4120-5507721-118<br>20455-118204-7761</div>
  <div class="footer-col abs" style="left:796px">0100-4410272<br>4120-5507721-118<br>20455-118204-7761</div>
</footer>

<div class="partner-badge abs" role="img" aria-label="Partner badge" style="left:459px;width:188px;height:56px;background:var(--badge-blue)"></div>
<div class="partner-badge abs" role="img" aria-label="Partner badge" style="left:706px;width:62px;height:62px;border-radius:50%;background:var(--badge-green)"></div>

</body>
</html>
```